Stoneline Benchworks Australia - Pool Flyer

G'day,Stoneline Benchworks Australia sells poolforms (https://www.stonelinebenchworksaustralia.com.au/index.php?route=product/category&path=17_61) The poolforms are reusable forms to pour a seamless concrete pool surround instead of using coping tiles. A much better look, less maintenance, and a modern architectural look .We're going to attend a pool and spa show but it is also about landscaping/surround as well. The forms we do make the concrete surround of a pool instead of tiles. I've put some text in a word doc and pictures as well. Feel free to use any words from our website and use/crop pics as you see fit.Any questions, more than happy to answer. We're thinking an A4 tri-fold flyer but happy for other suggestions as well. We're going to attend the show, speak to exhibitors, and hand them the flyer (and maybe a little promo thing too).

Target Market(s)

The target market is we are going to a pool and spa expo. The exhibitors install pools and do backyard landscaping. The flyer is for them.

Colors

Designer to choose colors to be used in the design.

Requirements
Must have
• The text/description of the poolforms and some of the pictures.
• Finished pictures.
• 1 or 2 of the forms (From the website).
• 1 of the Veil skimmer cap pictures (finished is probably better from the jpg with 3 images. probably best to crop and use 1 of the 3.
• Contact details of the website & email contact of sales@stonelinebenchworksaustralia.com.au + the phone number.

```html
<!DOCTYPE html>
<html lang="en">
<head>
<meta charset="utf-8">
<title>Stoneline Benchworks Australia – Pool Flyer</title>
<link rel="stylesheet" href="https://fonts.googleapis.com/css2?family=Open+Sans:wght@300;400;500;600;700&family=Arimo:wght@400;700&display=swap">
<style>
:root{
  --stage:#bdbdbd;
  --stage-deep:#9e9e9e;
  --charcoal:#474747;
  --paper:#f3f3f3;
  --paper-2:#e4e4e4;
  --ink:#333333;
  --ink-soft:#555555;
  --white:#ffffff;
  --rule:#8a8a8a;
  --pool-1:#1b3f9e;
  --pool-2:#4aa3d8;
  --deck-1:#d9d4cc;
  --deck-2:#a7a29a;
}
*{box-sizing:border-box;margin:0;padding:0}
html,body{width:1200px;height:4000px;overflow:hidden}
body{
  background:radial-gradient(ellipse at 50% 50%,var(--stage) 0%,var(--stage-deep) 100%);
  font-family:"Open Sans",sans-serif;color:var(--ink);
  display:flex;flex-direction:column;align-items:center;justify-content:center;gap:120px;
}
.spread{width:1100px;height:780px;display:flex;box-shadow:0 6px 24px rgba(0,0,0,.25)}
.panel{position:relative;width:366.67px;height:780px;overflow:hidden}
.panel svg.art{position:absolute;left:0;top:0}
.panel--light{background:linear-gradient(160deg,#f7f7f7,var(--paper))}
.panel--center{background:linear-gradient(90deg,var(--paper-2),#fafafa 45%,var(--paper-2))}
.panel--dark{background:var(--charcoal);color:var(--white)}

.lead{position:absolute;left:44px;top:44px;width:270px;font-size:19px;line-height:1.35;font-weight:500;color:var(--ink)}
.checks{position:absolute;left:44px;list-style:none;font-size:11px;line-height:1.45}
.checks li{display:flex;gap:12px;margin-bottom:18px}
.checks svg{flex:none;margin-top:2px}
.panel--light .checks{top:500px;width:290px;color:var(--ink-soft)}

.brand{display:flex;align-items:center;gap:12px}
.brand__mark{width:34px;height:34px;border-radius:50%;border:3px solid currentColor;flex:none}
.brand__name{font-size:11px;letter-spacing:.28em;line-height:1.45;font-weight:400;text-transform:uppercase}
.brand--center{position:absolute;left:0;right:0;top:280px;flex-direction:column;color:var(--ink);gap:10px}
.brand--center .brand__mark{width:54px;height:54px;border-width:4px}
.brand--center .brand__name{text-align:center;font-weight:600}
.brand--cover{position:absolute;left:60px;top:104px;color:var(--white)}

.contacts{position:absolute;left:0;right:0;top:520px;text-align:center;font-size:9.5px;color:var(--ink)}
.contacts p{margin:4px 0 18px}
.contacts svg{display:block;margin:0 auto}
.follow{font-weight:600;font-size:12px;margin-bottom:8px}
.social{display:flex;justify-content:center;gap:12px}
.social span{width:20px;height:20px;border-radius:50%;border:1px solid var(--ink)}

.cover-title{position:absolute;left:0;right:0;top:600px;text-align:center;font-family:"Arimo",sans-serif;line-height:1.12}
.cover-title .strong{font-size:29px;font-weight:700}
.cover-title .thin{font-size:23px;font-weight:400;color:#e6e6e6}
.cover-url{position:absolute;left:0;right:0;top:742px;text-align:center;font-size:9.5px;color:#e0e0e0}

.intro{position:absolute;left:26px;top:40px;width:320px;font-size:12.5px;line-height:1.5;font-weight:500}
.sub{position:absolute;left:26px;top:240px;font-size:12px;font-weight:600}
.sub::after{content:"";display:block;width:40px;height:2px;background:#9a9a9a;margin-top:3px}
.panel--dark .checks{top:280px;left:26px;width:320px;font-size:10px}
.panel--dark .checks li{margin-bottom:15px}

.heading{position:absolute;left:44px;font-size:19px;font-weight:600;color:var(--ink)}
.heading::after{content:"";display:block;width:38px;height:3px;background:var(--rule);margin-top:4px}
.product{position:absolute;left:44px;width:270px;font-size:10.5px;line-height:1.4;color:var(--ink)}
.product h3{font-size:12px;font-weight:500;margin-bottom:4px}
.product .price{margin-top:10px}
</style>
</head>
<body>

<!-- Outside spread -->
<section class="spread" aria-label="Flyer outside">
  <div class="panel panel--light">
    <svg class="art" width="367" height="780" viewBox="0 0 367 780">
      <defs><linearGradient id="g-pool-a" x1="0" y1="0" x2="1" y2="1"><stop offset="0" stop-color="#8fa9b6"/><stop offset=".45" stop-color="#5fb4e2"/><stop offset=".75" stop-color="#3e8fc6"/><stop offset="1" stop-color="#7d98a7"/></linearGradient></defs>
      <polygon role="img" aria-label="Photo of a seamless concrete pool edge beside clear blue water" fill="url(#g-pool-a)" points="0,160 367,150 367,440 270,405 183,450 96,405 0,440"/>
    </svg>
    <p class="lead">Get in touch with us to get your hands on the best pool formwork.</p>
    <ul class="checks">
      <li><svg width="11" height="11" viewBox="0 0 12 12"><circle cx="6" cy="6" r="5.2" fill="none" stroke="#555"/><path d="M3.5 6.2l1.8 1.8 3.2-3.6" fill="none" stroke="#555"/></svg>Form and pour a seamless<br>concrete pool surround</li>
      <li><svg width="11" height="11" viewBox="0 0 12 12"><circle cx="6" cy="6" r="5.2" fill="none" stroke="#555"/><path d="M3.5 6.2l1.8 1.8 3.2-3.6" fill="none" stroke="#555"/></svg>Architectural-designed look</li>
      <li><svg width="11" height="11" viewBox="0 0 12 12"><circle cx="6" cy="6" r="5.2" fill="none" stroke="#555"/><path d="M3.5 6.2l1.8 1.8 3.2-3.6" fill="none" stroke="#555"/></svg>Virtually no maintenance</li>
      <li><svg width="11" height="11" viewBox="0 0 12 12"><circle cx="6" cy="6" r="5.2" fill="none" stroke="#555"/><path d="M3.5 6.2l1.8 1.8 3.2-3.6" fill="none" stroke="#555"/></svg>Any Type of Concrete - Honed<br>Aggregate, Exposed Aggregate,<br>Grey or any colour concrete</li>
      <li><svg width="11" height="11" viewBox="0 0 12 12"><circle cx="6" cy="6" r="5.2" fill="none" stroke="#555"/><path d="M3.5 6.2l1.8 1.8 3.2-3.6" fill="none" stroke="#555"/></svg>Any Type of Pool - Fibreglass<br>and concrete pools</li>
    </ul>
  </div>

  <div class="panel panel--center">
    <svg class="art" width="367" height="780" viewBox="0 0 367 780" aria-hidden="true">
      <circle cx="183" cy="320" r="115" fill="none" stroke="#e2e2e2" stroke-width="26"/>
      <line x1="0" y1="270" x2="367" y2="180" stroke="#e6e6e6" stroke-width="1.5"/>
      <line x1="0" y1="370" x2="367" y2="280" stroke="#e6e6e6" stroke-width="1.5"/>
    </svg>
    <div class="brand brand--center"><span class="brand__mark"></span><span class="brand__name">Stoneline<br>Benchworks<br>Australia</span></div>
    <div class="contacts">
      <svg width="12" height="12" viewBox="0 0 12 12"><path d="M3 1l2 2.5-1.2 1.3a6 6 0 003.4 3.4L8.5 7 11 9l-1.3 1.8C5.5 10.8 1.2 6.5 1.2 2.3z" fill="none" stroke="#333"/></svg>
      <p>0400-555-019 / 0400-555-027</p>
      <svg width="12" height="10" viewBox="0 0 12 10"><rect x=".5" y=".5" width="11" height="9" fill="none" stroke="#333"/><path d="M.5 .5l5.5 5 5.5-5" fill="none" stroke="#333"/></svg>
      <p>sales@stonelinebenchworksaustralia.com.au</p>
      <svg width="12" height="12" viewBox="0 0 12 12"><circle cx="6" cy="6" r="5.3" fill="none" stroke="#333"/><ellipse cx="6" cy="6" rx="2.4" ry="5.3" fill="none" stroke="#333"/><line x1=".7" y1="6" x2="11.3" y2="6" stroke="#333"/></svg>
      <p>www.stonelinebenchworksaustralia.com.au</p>
      <div class="follow">Follow us</div>
      <div class="social"><span></span><span></span><span></span><span></span></div>
    </div>
  </div>

  <div class="panel panel--dark">
    <svg class="art" width="367" height="780" viewBox="0 0 367 780">
      <defs><linearGradient id="g-cover" x1="0" y1="0" x2="0" y2="1"><stop offset="0" stop-color="#8fb0c4"/><stop offset=".22" stop-color="#4c6650"/><stop offset=".42" stop-color="#2d3238"/><stop offset=".6" stop-color="var(--pool-1)"/><stop offset=".78" stop-color="var(--deck-1)"/><stop offset="1" stop-color="#bdb8ae"/></linearGradient></defs>
      <polygon role="img" aria-label="Photo of a kidney-shaped pool with a wide concrete surround in a backyard" fill="url(#g-cover)" points="0,236 183,177 367,236 367,600 0,600"/>
      <polygon fill="#6a6a6a" points="0,600 0,588 183,508 367,588 367,600"/>
      <polygon fill="var(--charcoal)" points="0,602 183,522 367,602 367,780 0,780"/>
    </svg>
    <div class="brand brand--cover"><span class="brand__mark"></span><span class="brand__name">Stoneline<br>Benchworks<br>Australia</span></div>
    <div class="cover-title">
      <div class="strong">THE BEST</div>
      <div class="thin">Seamless Pooledge</div>
      <div class="strong">FORMING SYSTEM</div>
    </div>
    <div class="cover-url">www.stonelinebenchworksaustralia.com.au</div>
  </div>
</section>

<!-- Inside spread -->
<section class="spread" aria-label="Flyer inside">
  <div class="panel panel--dark">
    <svg class="art" width="367" height="780" viewBox="0 0 367 780">
      <defs><linearGradient id="g-pool-b" x1="0" y1="0" x2="0" y2="1"><stop offset="0" stop-color="#2b2f33"/><stop offset=".35" stop-color="var(--pool-1)"/><stop offset=".62" stop-color="#3a6fd0"/><stop offset=".8" stop-color="#cfc9c0"/><stop offset="1" stop-color="var(--deck-2)"/></linearGradient></defs>
      <rect role="img" aria-label="Photo of a rectangular pool at dusk with exposed aggregate surround" x="0" y="500" width="367" height="280" fill="url(#g-pool-b)"/>
      <polygon fill="var(--charcoal)" points="0,498 367,498 367,512 183,578 0,512"/>
      <polyline fill="none" stroke="#5d5d5d" stroke-width="5" points="0,530 183,596 367,530"/>
    </svg>
    <p class="intro">Don't waste your time with fiddly, flimsy, or time consuming pool edge forming systems that end up in landfill. The L-Edge forms are made from strong PVC and can produce architectural designed looks that suit all types of pools.</p>
    <div class="sub">Advantages</div>
    <ul class="checks">
      <li><svg width="11" height="11" viewBox="0 0 12 12"><circle cx="6" cy="6" r="5.2" fill="none" stroke="#fff"/><path d="M3.5 6.2l1.8 1.8 3.2-3.6" fill="none" stroke="#fff"/></svg>Easy to use to create a seamless pooledge</li>
      <li><svg width="11" height="11" viewBox="0 0 12 12"><circle cx="6" cy="6" r="5.2" fill="none" stroke="#fff"/><path d="M3.5 6.2l1.8 1.8 3.2-3.6" fill="none" stroke="#fff"/></svg>An average sized pool can be formed up and<br>ready to for pouring in 2 hours</li>
      <li><svg width="11" height="11" viewBox="0 0 12 12"><circle cx="6" cy="6" r="5.2" fill="none" stroke="#fff"/><path d="M3.5 6.2l1.8 1.8 3.2-3.6" fill="none" stroke="#fff"/></svg>Forms are reusable and do not add to landfill</li>
      <li><svg width="11" height="11" viewBox="0 0 12 12"><circle cx="6" cy="6" r="5.2" fill="none" stroke="#fff"/><path d="M3.5 6.2l1.8 1.8 3.2-3.6" fill="none" stroke="#fff"/></svg>Made from tough PVC</li>
      <li><svg width="11" height="11" viewBox="0 0 12 12"><circle cx="6" cy="6" r="5.2" fill="none" stroke="#fff"/><path d="M3.5 6.2l1.8 1.8 3.2-3.6" fill="none" stroke="#fff"/></svg>Forms are both straight and bendable so no<br>problem for any shaped pool</li>
    </ul>
  </div>

  <div class="panel panel--light">
    <svg class="art" width="367" height="780" viewBox="0 0 367 780">
      <defs><linearGradient id="g-form" x1="0" y1="0" x2="1" y2="1"><stop offset="0" stop-color="#fafafa"/><stop offset=".6" stop-color="#e6e6e6"/><stop offset="1" stop-color="#d2d2d2"/></linearGradient></defs>
      <polygon fill="none" stroke="#333" stroke-width="1.5" points="44,82 244,82 272,110 272,254 72,254 44,226"/>
      <rect role="img" aria-label="Product photo of a straight white PVC pool edge form" x="50" y="88" width="216" height="160" fill="url(#g-form)"/>
      <polygon fill="none" stroke="#333" stroke-width="1.5" points="44,436 244,436 272,464 272,608 72,608 44,580"/>
      <rect role="img" aria-label="Product photo of a bendable white PVC pool edge form" x="50" y="442" width="216" height="160" fill="url(#g-form)"/>
    </svg>
    <div class="heading" style="top:30px">Pool Forms</div>
    <div class="product" style="top:276px">
      <h3>L-Edgeforms</h3>
      <p>L-Edgeform™ is a reusable PVC form used to create decorative concrete copings for swiming pools. Int..</p>
      <p class="price">$601.70<br>Ex Tax: $547.00</p>
    </div>
    <div class="product" style="top:630px">
      <h3>Bendable L-Edgeform</h3>
      <p>L-Edgeform™ is a reusable PVC form used to create decorative concrete copings for swiming pools. Int..</p>
      <p class="price">$729.30<br>Ex Tax: $663.00</p>
    </div>
  </div>

  <div class="panel panel--light">
    <svg class="art" width="367" height="780" viewBox="0 0 367 780">
      <defs><linearGradient id="g-pool-c" x1="0" y1="0" x2="0" y2="1"><stop offset="0" stop-color="#9fb6c8"/><stop offset=".3" stop-color="#2f3a2f"/><stop offset=".6" stop-color="#2f78c9"/><stop offset="1" stop-color="var(--deck-1)"/></linearGradient>
      <linearGradient id="g-deck" x1="0" y1="0" x2="1" y2="1"><stop offset="0" stop-color="#cfc9bf"/><stop offset=".5" stop-color="#b3aea5"/><stop offset="1" stop-color="#8e8a83"/></linearGradient>
      <linearGradient id="g-stone" x1="0" y1="0" x2="1" y2="1"><stop offset="0" stop-color="#8f939a"/><stop offset=".5" stop-color="#a9adb3"/><stop offset="1" stop-color="#5d6168"/></linearGradient></defs>
      <rect role="img" aria-label="Photo of a long blue pool beside a concrete deck" x="0" y="0" width="367" height="250" fill="url(#g-pool-c)"/>
      <polygon fill="#d6d6d6" points="0,250 0,236 183,163 367,236 367,250"/>
      <polygon fill="#f3f3f3" points="0,250 183,177 367,250 367,780 0,780"/>
      <polygon fill="none" stroke="#333" stroke-width="1.5" points="40,354 296,354 324,382 324,551 68,551 40,523"/>
      <rect role="img" aria-label="Photo of a concealed skimmer cap set flush in exposed aggregate concrete" x="46" y="360" width="272" height="185" fill="url(#g-deck)"/>
      <polygon fill="none" stroke="#333" stroke-width="1.5" points="40,571 296,571 324,599 324,758 68,758 40,730"/>
      <rect role="img" aria-label="Photo of a polished concrete surround with an ice bucket and glasses" x="46" y="577" width="272" height="175" fill="url(#g-stone)"/>
    </svg>
    <div class="heading" style="top:296px">Veil Skimmer Cap</div>
  </div>
</section>

</body>
</html>
```